Brindle Grass Services website design

We want to create a Sports turf website for our business Brindle Grass Services - we do sports turf management on sports fields around the Harbourvale region soccer rugby league softball fields etc from full turf management plans and maintenance to just supply and apply of turf management products and just supply of products with program we also do grounds facility maintenance at council facility's and grounds that require a higher level of care - we will up load our logos and fonts etc to assist with the colour pallet for the website - we will have to have a landing page a shop page with tabs a gallery tab along with a grants initiative and our coastals finest green tab also - our font for the txt is called ethnocentric
Updates

how do we open time for people to submit we have no one submitted

Industry/Entity Type

Turf

Coding

Coded - Design and coding required

Number of Pages Required

5+ page

Font styles to use
Other font styles liked:
• ethnocentric

Requirements
Must have
• I have mentioned some waffle in the description that should assist
Should not have
• anything not related

```html
<!DOCTYPE html>
<html lang="en">
<head>
<meta charset="utf-8">
<title>Brindle Grass Services — Sports Turf Management</title>
<link href="https://fonts.googleapis.com/css2?family=Orbitron:wght@700;900&family=Poppins:wght@400;500;600;700&display=swap" rel="stylesheet">
<style>
:root{
  --ink:#0c0d0e;
  --ink-2:#151718;
  --ink-3:#1d2022;
  --green:#2eaa3d;
  --green-deep:#1f8a2e;
  --green-bright:#46c955;
  --cyan:#27b5ef;
  --blue:#19a4e6;
  --white:#ffffff;
  --muted:#b9c0c4;
  --line:rgba(255,255,255,.14);
  --head:'Orbitron',sans-serif;
  --body:'Poppins',sans-serif;
}
*{box-sizing:border-box;margin:0;padding:0}
html,body{width:1200px;height:5220px;overflow:hidden}
body{background:var(--ink);color:var(--white);font-family:var(--body);font-size:13px;line-height:1.55;position:relative}
h1,h2,h3{font-family:var(--head);font-weight:900;text-transform:uppercase;letter-spacing:1px}
.accent{color:var(--cyan)}
.btn{display:inline-block;background:var(--green);color:var(--white);font-family:var(--body);font-weight:600;font-size:11px;text-transform:uppercase;letter-spacing:.5px;padding:11px 20px;border-radius:4px}
.btn-outline{background:transparent;border:1px solid var(--white)}
.ph{display:block}
section{position:absolute;left:0;width:1200px}

/* header */
.site-header{position:absolute;top:18px;left:120px;width:960px;height:44px;display:flex;align-items:center;justify-content:space-between;z-index:5}
.brand{font-family:var(--head);font-weight:900;font-size:17px;color:var(--white);display:flex;align-items:center;gap:10px;letter-spacing:1px}
.brand-dot{width:12px;height:12px;background:var(--green);flex:none}
.main-nav{display:flex;align-items:center;gap:26px;font-size:11px;font-weight:600;text-transform:uppercase}
.main-nav .btn{padding:9px 16px}

/* hero */
.hero{top:0;height:600px;overflow:hidden}
.hero-photo{position:absolute;inset:0;background:radial-gradient(ellipse at 64% 40%,#3a4a52 0%,#1a2226 38%,#0c0f10 75%)}
.hero-copy{position:absolute;left:120px;top:160px;width:560px}
.hero-copy h1{font-size:52px;line-height:1.08}
.hero-copy p{margin:22px 0 26px;width:380px;color:var(--muted);font-size:13px}
.hero-curve{position:absolute;left:0;bottom:0}

/* about */
.about{top:600px;height:620px;overflow:hidden}
.about-photo{position:absolute;left:120px;top:110px;width:460px;height:400px;background:linear-gradient(180deg,#7fb6de 0%,#5d8a6c 45%,#2f7a36 70%,#1f4d26 100%);border-radius:6px 60px 6px 6px}
.about-photo .slats{position:absolute;inset:0}
.about-copy{position:absolute;left:640px;top:110px;width:440px}
.about-copy h2{font-size:32px;line-height:1.15}
.about-copy p{margin:16px 0;color:var(--muted);font-size:12px}
.about-list{list-style:none;margin-bottom:20px}
.about-list li{display:flex;gap:10px;align-items:center;margin-bottom:7px;font-size:12px}
.tick{width:14px;height:14px;flex:none}
.ghost-word{position:absolute;left:0;top:528px;width:1200px;text-align:center;font-family:var(--head);font-weight:900;font-size:70px;line-height:1;color:rgba(255,255,255,.05);white-space:nowrap;letter-spacing:2px}

/* services */
.services{top:1180px;height:940px;background:var(--green)}
.services-top{position:absolute;left:0;top:-1px}
.section-title{position:absolute;left:0;width:1200px;text-align:center;font-size:32px}
.services .section-title{top:120px}
.service-grid{position:absolute;left:120px;top:180px;width:960px;display:grid;grid-template-columns:470px 470px;gap:20px}
.service-card{background:var(--white);border-radius:8px;padding:8px;height:310px;display:flex;flex-direction:column}
.service-card h3{font-family:var(--body);font-weight:600;text-transform:none;letter-spacing:0;color:var(--ink);font-size:15px;text-align:center;padding:6px 0 10px}
.service-card .ph{flex:1;border-radius:6px}
.services .btn-outline{position:absolute;left:525px;top:858px}

/* why */
.why{top:2120px;height:500px;background:var(--ink)}
.why h2{position:absolute;left:120px;top:100px;font-size:32px;line-height:1.15;width:620px}
.why-grid{position:absolute;left:120px;top:200px;width:700px;display:grid;grid-template-columns:1fr 1fr;gap:30px 40px}
.why-item{display:flex;gap:14px}
.why-icon{width:40px;height:40px;background:var(--green);border-radius:6px;flex:none;display:flex;align-items:center;justify-content:center}
.why-item h4{font-size:14px;font-weight:600;margin-bottom:4px}
.why-item p{color:var(--muted);font-size:12px}
.why-photo{position:absolute;left:880px;top:80px;width:200px;height:290px;border-radius:10px;background:linear-gradient(180deg,#cfd6da 0%,#8e9aa0 40%,#4f6f42 70%,#2f4c2a 100%)}

/* how */
.how{top:2620px;height:380px;background:linear-gradient(180deg,#0c0d0e 0%,#1b2a1a 45%,#2c4a22 100%)}
.how .section-title{top:40px}
.how-band{position:absolute;left:120px;top:110px;width:960px;height:210px;display:flex;border-radius:10px;overflow:hidden}
.how-step{flex:1;text-align:center;padding:54px 30px 0}
.how-step:nth-child(1){background:var(--green-deep)}
.how-step:nth-child(2){background:var(--green)}
.how-step:nth-child(3){background:var(--green-bright)}
.how-step h4{font-size:15px;font-weight:600;margin:10px 0 6px}
.how-step p{font-size:12px}

/* gallery */
.gallery{top:3000px;height:460px;background:var(--ink)}
.gallery .section-title{top:0}
.gallery-track{position:absolute;left:120px;top:60px;width:960px;height:400px;display:flex;gap:12px;align-items:stretch}
.gallery-side{width:140px;background:linear-gradient(180deg,#2a2d2f,#161819);border-radius:6px}
.gallery-main{flex:1;position:relative;border-radius:6px;overflow:hidden;display:flex}
.gallery-before{flex:1;background:linear-gradient(160deg,#6b6a3b,#4b5a2a 50%,#3d4a24)}
.gallery-after{flex:1;background:linear-gradient(160deg,#3f8f3a,#2e7a2c 50%,#246a24)}
.gallery-tag{position:absolute;top:12px;font-size:12px;font-weight:600;text-transform:uppercase}
.gallery-divider{position:absolute;left:50%;top:0;bottom:0;width:2px;background:var(--white)}
.gallery-knob{position:absolute;left:50%;top:50%;width:30px;height:30px;margin:-15px 0 0 -15px;border-radius:50%;background:var(--white)}
.gallery-arrow{position:absolute;top:245px;width:28px;height:28px}

/* products */
.products{top:3460px;height:790px;background:var(--blue)}
.products .section-title{top:60px}
.product-col{position:absolute;left:120px;top:130px;width:470px;display:flex;flex-direction:column;gap:20px}
.product-card{background:var(--white);color:var(--ink);border-radius:10px;display:flex;gap:16px;padding:16px;height:270px;position:relative}
.product-card .ph{width:200px;border-radius:6px;flex:none}
.product-info{padding-top:20px}
.product-info h4{font-size:17px;font-weight:700;line-height:1.25;margin-bottom:8px}
.product-info p{font-size:12px;color:#444b50;margin-bottom:14px}
.price{position:absolute;width:54px;height:54px;border-radius:50%;background:var(--green);color:var(--white);font-weight:700;font-size:13px;display:flex;align-items:center;justify-content:center}
.product-feature{position:absolute;left:610px;top:130px;width:470px;height:560px;background:var(--white);color:var(--ink);border-radius:10px;padding:16px}
.product-feature .ph{height:400px;border-radius:6px}
.product-feature h4{font-size:18px;font-weight:700;margin:16px 0 4px}
.product-feature p{font-size:12px;color:#444b50;width:300px}
.product-feature .btn{position:absolute;right:20px;bottom:34px}
.products .btn-outline{position:absolute;left:513px;top:712px}

/* contact */
.contact{top:4250px;height:450px;background:var(--ink)}
.contact-form{position:absolute;left:120px;top:60px;width:500px;height:340px;background:var(--white);border-radius:10px;padding:70px 24px 20px;color:var(--ink)}
.contact-form h2{position:absolute;left:0;top:0;width:500px;height:54px;background:var(--ink-2);color:var(--white);border-radius:10px 10px 0 0;font-size:24px;text-align:center;line-height:54px}
.form-row{display:grid;grid-template-columns:1fr 1fr;gap:14px;margin-bottom:14px}
.field{height:36px;border:1px solid #cfd4d7;border-radius:4px;font-size:11px;color:#555;padding:8px 10px}
.field.area{height:80px}
.contact-form .btn{position:absolute;right:24px;bottom:22px}
.contact-photo{position:absolute;left:650px;top:40px;width:430px;height:380px;border-radius:14px 80px 14px 14px;background:linear-gradient(180deg,#3a3f42,#24292b 55%,#2f4a36)}

/* cta */
.cta{top:4720px;left:120px;width:960px;height:240px;background:linear-gradient(90deg,var(--green-deep),var(--green-bright));border-radius:14px;overflow:hidden}
.cta-panel{position:absolute;left:30px;top:30px;width:380px;height:180px;border-radius:10px;background:rgba(255,255,255,.12)}
.cta-copy{position:absolute;left:480px;top:42px;width:440px}
.cta-copy h2{font-size:27px;line-height:1.15}
.cta-copy p{font-size:12px;margin:10px 0 16px}
.cta-actions{display:flex;gap:22px;align-items:center}
.cta-phone{display:flex;gap:10px;align-items:center;font-weight:700;font-size:22px}

/* footer */
.site-footer{position:absolute;top:4990px;left:0;width:1200px;height:230px;background:var(--ink)}
.footer-cols{position:absolute;left:120px;top:20px;width:960px;display:grid;grid-template-columns:200px 140px 200px 190px 230px}
.footer-cols h5{font-family:var(--head);font-size:12px;text-transform:uppercase;margin-bottom:12px;letter-spacing:1px}
.footer-cols p,.footer-cols li{font-size:11px;color:var(--muted);list-style:none;margin-bottom:5px}
.footer-cols .brand{font-size:13px;margin-bottom:10px}
.social{display:flex;gap:8px;margin-top:10px}
.social span{width:22px;height:22px;border-radius:50%;border:1px solid var(--muted)}
.subscribe{display:flex;gap:6px;margin-top:10px}
.subscribe .field{height:32px;width:140px;background:var(--ink-3);border-color:var(--line);color:var(--muted)}
.subscribe .btn{padding:8px 12px}
.contact-line{display:flex;gap:8px;align-items:center}
.copyright{position:absolute;left:0;bottom:14px;width:1200px;text-align:center;font-size:10px;color:var(--muted);border-top:1px solid var(--line);padding-top:10px}
</style>
</head>
<body>

<header class="site-header">
  <div class="brand"><span class="brand-dot"></span>Brindle Grass Services</div>
  <nav class="main-nav">
    <span>Services</span><span>About Us</span><span>Shop</span><span>Gallery</span><span>Grants &amp; Initiatives</span>
    <span class="btn">Contact Us</span>
  </nav>
</header>

<section class="hero">
  <div class="hero-photo ph" role="img" aria-label="Rugby league player holding a ball on a floodlit sports field"></div>
  <div class="hero-copy">
    <h1><span class="accent">Performance</span><br>Starts From<br>The Ground Up</h1>
    <p>From local sports clubs to major council facilities, Brindle Grass Services delivers professional turf care and facility maintenance with precision, reliability and results that stand up to game day.</p>
    <span class="btn">Get Your Free Estimate Today</span>
  </div>
  <svg class="hero-curve" width="1200" height="90" viewBox="0 0 1200 90">
    <path d="M0 40 Q600 110 1200 40 L1200 90 L0 90 Z" fill="#0c0d0e"/>
    <path d="M0 40 Q600 110 1200 40" fill="none" stroke="#2eaa3d" stroke-width="6"/>
  </svg>
</section>

<section class="about">
  <div class="about-photo ph" role="img" aria-label="Sports stadium field viewed through vertical grandstand slats">
    <svg class="slats" width="460" height="400" viewBox="0 0 460 400">
      <g fill="#0c0d0e">
        <rect x="70" y="0" width="10" height="400"/><rect x="150" y="0" width="10" height="400"/>
        <rect x="230" y="0" width="10" height="400"/><rect x="310" y="0" width="10" height="400"/>
        <rect x="390" y="0" width="10" height="400"/>
      </g>
    </svg>
  </div>
  <div class="about-copy">
    <h2>About Brindle Grass<br><span class="accent">Services</span></h2>
    <p>At Brindle Grass Services, we're passionate about growing and maintaining world-class sports turf across the Harbourvale region. With years of local experience, we provide end-to-end solutions, from turf maintenance programs to product supply and facility care for councils, schools and sporting clubs.</p>
    <ul class="about-list">
      <li><svg class="tick" viewBox="0 0 14 14"><circle cx="7" cy="7" r="7" fill="#2eaa3d"/><path d="M4 7.2l2 2 4-4.2" stroke="#fff" stroke-width="1.6" fill="none"/></svg>Local experts serving Harbourvale's sports fields and clubs</li>
      <li><svg class="tick" viewBox="0 0 14 14"><circle cx="7" cy="7" r="7" fill="#2eaa3d"/><path d="M4 7.2l2 2 4-4.2" stroke="#fff" stroke-width="1.6" fill="none"/></svg>Complete turf management &amp; maintenance programs</li>
      <li><svg class="tick" viewBox="0 0 14 14"><circle cx="7" cy="7" r="7" fill="#2eaa3d"/><path d="M4 7.2l2 2 4-4.2" stroke="#fff" stroke-width="1.6" fill="none"/></svg>High-quality turf products and application services</li>
      <li><svg class="tick" viewBox="0 0 14 14"><circle cx="7" cy="7" r="7" fill="#2eaa3d"/><path d="M4 7.2l2 2 4-4.2" stroke="#fff" stroke-width="1.6" fill="none"/></svg>Grounds &amp; facility maintenance for councils and venues</li>
    </ul>
    <span class="btn">Learn More About Us</span>
  </div>
  <div class="ghost-word">BRINDLE GRASS SERVICES</div>
</section>

<section class="services">
  <svg class="services-top" width="1200" height="60" viewBox="0 0 1200 60">
    <path d="M0 0 L1200 0 L1200 10 Q600 70 0 10 Z" fill="#0c0d0e"/>
  </svg>
  <h2 class="section-title">Our Services</h2>
  <div class="service-grid">
    <div class="service-card"><h3>Sports Turf Management</h3><div class="ph" role="img" aria-label="Players training on a well-kept sports field" style="background:linear-gradient(180deg,#9cc4dd,#4f9a45 45%,#3a8032)"></div></div>
    <div class="service-card"><h3>Product Supply &amp; Application</h3><div class="ph" role="img" aria-label="Worker checking boxes of turf products in a warehouse" style="background:linear-gradient(160deg,#c9b08a,#5d7a96 50%,#2f4f6e)"></div></div>
    <div class="service-card"><h3>Grounds &amp; Facility Maintenance</h3><div class="ph" role="img" aria-label="Freshly laid turf rolls at a council facility" style="background:linear-gradient(180deg,#8fb5cf,#6f8f4e 45%,#4a7a30)"></div></div>
    <div class="service-card"><h3>Custom Turf Programs</h3><div class="ph" role="img" aria-label="Consultant planning a turf program on a laptop" style="background:linear-gradient(160deg,#d8dcdf,#6c7276 50%,#3f7a34)"></div></div>
  </div>
  <span class="btn btn-outline">View All Services</span>
</section>

<section class="why">
  <h2>Why Choose Brindle<br>Grass <span class="accent">Services</span></h2>
  <div class="why-grid">
    <div class="why-item"><div class="why-icon"><svg width="20" height="20" viewBox="0 0 20 20"><path d="M10 2a6 6 0 0 0-6 6c0 4.5 6 10 6 10s6-5.5 6-10a6 6 0 0 0-6-6zm0 8.2a2.2 2.2 0 1 1 0-4.4 2.2 2.2 0 0 1 0 4.4z" fill="#fff"/></svg></div><div><h4>Local Expertise</h4><p>We live and work in the Harbourvale region, so we understand the local conditions and what it takes to keep fields thriving year-round.</p></div></div>
    <div class="why-item"><div class="why-icon"><svg width="20" height="20" viewBox="0 0 20 20"><path d="M4 10.5l4 4 8-9" stroke="#fff" stroke-width="2.4" fill="none"/></svg></div><div><h4>Professional Standards</h4><p>Our turf care programs are guided by industry best practice, delivering results you can count on season after season.</p></div></div>
    <div class="why-item"><div class="why-icon"><svg width="20" height="20" viewBox="0 0 20 20"><rect x="3" y="6" width="14" height="11" rx="1.5" fill="#fff"/><rect x="7" y="3" width="6" height="4" fill="none" stroke="#fff" stroke-width="1.6"/></svg></div><div><h4>Quality Products &amp; Equipment</h4><p>We use premium turf management products and professional-grade equipment to ensure healthy, durable playing surfaces.</p></div></div>
    <div class="why-item"><div class="why-icon"><svg width="20" height="20" viewBox="0 0 20 20"><circle cx="10" cy="10" r="7" fill="none" stroke="#fff" stroke-width="2"/><circle cx="10" cy="10" r="2.6" fill="#fff"/></svg></div><div><h4>Tailored Solutions</h4><p>Every field is unique. We design turf programs that match your budget, usage and performance goals.</p></div></div>
  </div>
  <div class="why-photo ph" role="img" aria-label="Groundskeeper operating a turf machine on a field"></div>
</section>

<section class="how">
  <h2 class="section-title">How It Works</h2>
  <div class="how-band">
    <div class="how-step"><svg width="26" height="26" viewBox="0 0 26 26"><circle cx="11" cy="11" r="7" fill="none" stroke="#fff" stroke-width="2.4"/><path d="M16 16l6 6" stroke="#fff" stroke-width="2.4"/></svg><h4>Site Assessment</h4><p>We inspect your field's condition, soil health and current turf performance.</p></div>
    <div class="how-step"><svg width="26" height="26" viewBox="0 0 26 26"><rect x="5" y="3" width="16" height="20" rx="2" fill="none" stroke="#fff" stroke-width="2.2"/><path d="M9 10h8M9 14h8M9 18h5" stroke="#fff" stroke-width="2"/></svg><h4>Tailored Program</h4><p>We design a customised management plan to ensure the best turf quality possible.</p></div>
    <div class="how-step"><svg width="26" height="26" viewBox="0 0 26 26"><path d="M5 13.5l5 5 11-12" stroke="#fff" stroke-width="2.6" fill="none"/></svg><h4>Implementation &amp; Support</h4><p>From supply to application, we provide ongoing care &amp; monitoring for lasting results.</p></div>
  </div>
</section>

<section class="gallery">
  <h2 class="section-title">Our Project <span class="accent">Gallery</span></h2>
  <div class="gallery-track">
    <div class="gallery-side ph" role="img" aria-label="Previous project photo"></div>
    <div class="gallery-main">
      <div class="gallery-before ph" role="img" aria-label="Worn patchy turf before renovation"></div>
      <div class="gallery-after ph" role="img" aria-label="Lush green turf after renovation"></div>
      <span class="gallery-tag" style="left:16px">Before</span>
      <span class="gallery-tag" style="right:16px">After</span>
      <div class="gallery-divider"></div>
      <div class="gallery-knob"></div>
    </div>
    <div class="gallery-side ph" role="img" aria-label="Next project photo"></div>
  </div>
  <svg class="gallery-arrow" style="left:80px" viewBox="0 0 28 28"><circle cx="14" cy="14" r="14" fill="#fff"/><path d="M16 8l-6 6 6 6" stroke="#0c0d0e" stroke-width="2.4" fill="none"/></svg>
  <svg class="gallery-arrow" style="left:1092px" viewBox="0 0 28 28"><circle cx="14" cy="14" r="14" fill="#fff"/><path d="M12 8l6 6-6 6" stroke="#0c0d0e" stroke-width="2.4" fill="none"/></svg>
</section>

<section class="products">
  <h2 class="section-title">Featured Turf Products</h2>
  <div class="product-col">
    <div class="product-card">
      <div class="ph" role="img" aria-label="Liquid wetting agent containers" style="background:linear-gradient(180deg,#e7eef2,#9fc7a2)"></div>
      <div class="product-info"><h4>HydroRoot Liquid Wetting Agent</h4><p>Improves water infiltration and retention for healthier, greener sports turf.</p><span class="btn">Shop Now</span></div>
      <span class="price" style="left:170px;top:150px">$25.19</span>
    </div>
    <div class="product-card">
      <div class="ph" role="img" aria-label="Granular insecticide bag" style="background:linear-gradient(180deg,#eef1ee,#8fbf86)"></div>
      <div class="product-info"><h4>Grubguard GR</h4><p>Proven grub and pest protection for sports fields and lawns, long lasting control.</p><span class="btn">Shop Now</span></div>
      <span class="price" style="right:16px;top:16px">$25.19</span>
    </div>
  </div>
  <div class="product-feature">
    <div class="ph" role="img" aria-label="Tub of turf treatment product on a store shelf" style="background:linear-gradient(180deg,#3a3d3f,#c8b24a 55%,#6f9a3e)"></div>
    <span class="price" style="right:30px;top:30px">$25.19</span>
    <h4>TurfShield</h4>
    <p>Improves turf colour and resilience, supporting dense recovery and stronger root growth.</p>
    <span class="btn">Shop Now</span>
  </div>
  <span class="btn btn-outline">View All Products</span>
</section>

<section class="contact">
  <div class="contact-form">
    <h2>Get In Touch</h2>
    <div class="form-row"><div class="field">First Name*</div><div class="field">Last Name*</div></div>
    <div class="form-row"><div class="field">Email*</div><div class="field">Phone*</div></div>
    <div class="field area">Message*</div>
    <span class="btn">Submit</span>
  </div>
  <div class="contact-photo ph" role="img" aria-label="Shop interior with turf products on shelves"></div>
</section>

<section class="cta">
  <div class="cta-panel" role="img" aria-label="Brand graphic area"></div>
  <div class="cta-copy">
    <h2>Let's Keep Your<br>Turf In Top Shape</h2>
    <p>Ready to improve your field's performance and presentation? Contact us today for a free consultation or site visit.</p>
    <div class="cta-actions">
      <span class="btn btn-outline">Call Us Today</span>
      <span class="cta-phone"><svg width="22" height="22" viewBox="0 0 22 22"><path d="M5 2l4 4-2 3a11 11 0 0 0 6 6l3-2 4 4-3 3C9 20 2 13 2 5z" fill="#fff"/></svg>(555) 014-2290</span>
    </div>
  </div>
</section>

<footer class="site-footer">
  <div class="footer-cols">
    <div>
      <div class="brand"><span class="brand-dot"></span>Brindle Grass Services</div>
      <p>Based in the Harbourvale region, Brindle Grass Services specialises in turf solutions for sports facilities, councils and private grounds.</p>
      <div class="social"><span></span><span></span><span></span></div>
    </div>
    <div><h5>Quick Links</h5><ul><li>Home</li><li>Services</li><li>About Us</li><li>Shop</li><li>Gallery</li><li>Grants &amp; Initiatives</li><li>Contact Us</li></ul></div>
    <div><h5>Contact Us</h5>
      <p class="contact-line"><svg width="12" height="12" viewBox="0 0 22 22"><path d="M5 2l4 4-2 3a11 11 0 0 0 6 6l3-2 4 4-3 3C9 20 2 13 2 5z" fill="#2eaa3d"/></svg>(555) 014-2290</p>
      <p class="contact-line"><svg width="12" height="12" viewBox="0 0 20 20"><path d="M10 2a6 6 0 0 0-6 6c0 4.5 6 10 6 10s6-5.5 6-10a6 6 0 0 0-6-6z" fill="#2eaa3d"/></svg>Harbourvale Region</p>
      <p class="contact-line"><svg width="12" height="12" viewBox="0 0 20 20"><rect x="2" y="4" width="16" height="12" rx="2" fill="#2eaa3d"/></svg>info@brindlegrass.example</p>
    </div>
    <div><h5>Services</h5><ul><li>Sports Turf Management</li><li>Product Supply &amp; Application</li><li>Grounds &amp; Facility Maintenance</li><li>Custom Turf Programs</li></ul></div>
    <div><h5>Follow Us On</h5><p>Get turf tips and product news.</p>
      <div class="subscribe"><div class="field">Enter Your Email</div><span class="btn">Submit</span></div>
    </div>
  </div>
  <div class="copyright">© 2025 Brindle Grass Services. All Rights Reserved.</div>
</footer>

</body>
</html>
```